Postcard Design Project A Healthy reminder

Dr.'s Jeetesh and Lorna sethi. Internal Medicine/Family practice. This postcard will be for our patients that we have not seen in a while. Also we need another postcard (the one your designing) with a different heading for New patient's. Do you offer a price break for that? The only thing we would need to change is the heading. Please let me know. Thank you so much! Also can you use the map on the last postcard and our logo I made? I cant find it. Please feel free to call me or email me.

```html
<!DOCTYPE html>
<html lang="en">
<head>
<meta charset="utf-8">
<title>Now Accepting New Patients – Postcard</title>
<link rel="stylesheet" href="https://fonts.googleapis.com/css2?family=Tenor+Sans&family=Arimo:wght@400;700&display=swap">
<style>
  :root {
    --brand-red: #961b1f;
    --ink-black: #0d0d0d;
    --paper: #ffffff;
    --text-grey: #3a3a3a;
    --photo-wall: #d8c3ae;
    --photo-light: #f1ece6;
    --photo-coat: #e9e7e4;
    --photo-floor: #b7aea3;
    --photo-dark: #8f7b68;
  }
  html, body {
    margin: 0;
    padding: 0;
    width: 1200px;
    height: 817px;
    overflow: hidden;
    background: var(--paper);
  }
  .postcard {
    position: relative;
    width: 1200px;
    height: 817px;
    overflow: hidden;
    background: var(--paper);
    font-family: "Arimo", Arial, sans-serif;
  }
  .postcard__shapes {
    position: absolute;
    inset: 0;
    width: 1200px;
    height: 817px;
  }
  .headline {
    position: absolute;
    margin: 0;
    font-family: "Tenor Sans", "Gill Sans", sans-serif;
    font-weight: 400;
    color: var(--paper);
    line-height: 1;
    white-space: nowrap;
  }
  .headline--now { left: 178px; top: 64px; font-size: 66px; }
  .headline--accepting { left: 112px; top: 126px; font-size: 62px; }
  .headline--patients { left: 298px; top: 186px; font-size: 92px; }

  .practice-mark {
    position: absolute;
    left: 66px;
    top: 398px;
    width: 92px;
    height: 92px;
    background: var(--brand-red);
  }
  .practice-name {
    position: absolute;
    left: 176px;
    top: 404px;
    margin: 0;
    font-size: 34px;
    font-weight: 700;
    line-height: 40px;
    color: var(--ink-black);
  }
  .practice-tagline {
    position: absolute;
    left: 117px;
    top: 564px;
    margin: 0;
    font-size: 15px;
    font-weight: 700;
    letter-spacing: 1.5px;
    color: var(--ink-black);
  }
  .practice-address {
    position: absolute;
    left: 74px;
    top: 618px;
    margin: 0;
    font-style: normal;
    font-size: 28px;
    font-weight: 700;
    line-height: 37px;
    color: var(--text-grey);
  }
  .contact-bar {
    position: absolute;
    left: 72px;
    top: 726px;
    margin: 0;
    font-size: 35px;
    font-weight: 700;
    letter-spacing: 3.4px;
    color: var(--paper);
    white-space: nowrap;
  }
  .contact-bar__divider { padding: 0 8px; }
</style>
</head>
<body>
<main class="postcard">
  <svg class="postcard__shapes" viewBox="0 0 902 614" preserveAspectRatio="none">
    <defs>
      <linearGradient id="photoTone" x1="0" y1="0" x2="1" y2="0">
        <stop offset="0" stop-color="var(--photo-wall)"/>
        <stop offset="0.3" stop-color="var(--photo-light)"/>
        <stop offset="0.55" stop-color="var(--photo-coat)"/>
        <stop offset="0.8" stop-color="var(--photo-wall)"/>
        <stop offset="1" stop-color="var(--photo-dark)"/>
      </linearGradient>
      <linearGradient id="photoShade" x1="0" y1="0" x2="0" y2="1">
        <stop offset="0" stop-color="#000" stop-opacity="0"/>
        <stop offset="0.7" stop-color="var(--photo-floor)" stop-opacity="0.25"/>
        <stop offset="1" stop-color="var(--photo-dark)" stop-opacity="0.5"/>
      </linearGradient>
    </defs>
    <g class="photo-area" role="img" aria-label="Photo of two doctors in white coats reviewing a patient chart in a clinic hallway">
      <path d="M600,0 L902,0 L902,614 L740,614 C640,480 520,390 425,328 C505,245 575,140 600,0 Z" fill="url(#photoTone)"/>
      <path d="M600,0 L902,0 L902,614 L740,614 C640,480 520,390 425,328 C505,245 575,140 600,0 Z" fill="url(#photoShade)"/>
    </g>
    <path class="red-swoosh"
          d="M0,0 L605,0 C578,148 505,258 415,332 C300,248 155,176 0,166 Z"
          fill="var(--brand-red)"/>
    <path class="swoosh-edge" d="M0,166 C155,176 300,248 415,332" fill="none" stroke="var(--ink-black)" stroke-width="2"/>
    <path class="black-band"
          d="M415,332 C420,330 423,329 425,328 C520,390 640,480 740,614 L0,614 L0,528 L576,528 C530,455 480,385 415,332 Z"
          fill="var(--ink-black)"/>
  </svg>

  <h1 class="headline headline--now">Now</h1>
  <p class="headline headline--accepting">Accepting New</p>
  <p class="headline headline--patients">Patients</p>

  <div class="practice-mark" aria-hidden="true"></div>
  <p class="practice-name">Jeetesh T Sethi,<br>M.D.</p>
  <p class="practice-tagline">A Primary Care Office</p>

  <address class="practice-address">
    4820 W. Alder Avenue Suite 210<br>
    Fresno, Ca 93711
  </address>

  <p class="contact-bar">(555) 014-2270<span class="contact-bar__divider">|</span>www.sethimd.com</p>
</main>
</body>
</html>
```